Web Design Project

The project is about a web design for a brand new dental clinic: Orla Dental Clinic. The dental clinic is located in NSW and the target market is population of all ages (although specialised pediatric dentistry will not be offered at the clinic)
The design is to be:
• Modern
• Professional
• Simple but very attractive
• Logically organised
• Clean
• Fresh
• Engaging
• Friendly
• Creative
Design is to have:
• The dental clinic logo to be shown at the top of every page
• The address and phone number also to be shown at the top of every page
• A link for an online appointment on all pages
• Easy to navigate pages
• Tabs which are easy to identify and read. The tabs are also to be shown at the bottom of each page.
• With drop down menus to be displayed as you scroll along tabs
• Text that is easy to read
• A good use of the colour
• Photos of people smiling. These photos are to be very selective, meaningful and fresh as they play an important role suggesting excellent dental health.
• Short messages
The design is NOT to have:
- Similarities with any other dental clinic (the web design should be authentic and genuine)
- Photos of teeth or smiles on their own or dentists practising the dental work on patients
The site is to include the following pages:
• HOME – this is the welcome page. This page will contain a thank you message and an invitation to visit the dental clinic. It will also have a follow us on chatterbox and quillpost and an area to display testimonials.
• ABOUT US – this page will contain a summary of who we are and the business mission.
• OUR SERVICES – this page is to include a list of the different dental treatments that will be provided at the clinic. Each treatment will have a link to a small window containing a brief description of what the treatment is. This page will also have a section for guarantees on dental work.
• OUR TEAM – this page will have a photo of the professionals that will be working at the clinic and which includes dentists, dental hygienist, dental assistant and administrative assistant.
• OUR TECHNOLOGY – this page will show equipment and technology that we have available at the clinic.
• GALLERY – on this page we will display the ‘before’ and ‘after’ of different treatments conducted, photos of the clinic, etc.
• SPECIAL OFFERS – this page is to contain a list of the discounts available. This page is to include an area to display special offers that will be offered in addition to standard discounts. This page must also include an option for the client to subscribe to our special offers/updates via email. It must also include payment options. It must also include a voucher design which can be printed for discounts.
• LATEST NEWS – this page will include information on latest technical advances on the dental field and may also have links to other documents
• CONTACT US – this page must include:
o the name of the clinic, full address, phone number, fax number, email address
o the business hours
o a location map – link to roamchart
o an option under: Using public transport? Plan your trip at: www.transitplanr.example.au
o an option under: Driving your vehicle? Obtain trip directions at: www.routeduo.example.au
o parking availability
o a ‘print this page’ option
o a photo of the premises for easy identification of the location
• ONLINE APPOINTMENTS – this page must include cells for:
o name
o surname
o mobile number, alternative phone number, email address
o best contact: mobile/alternative number/email
o preferred date and preferred time of the appointment
o are you an existing client/a new patient?
o describe any special needs you may have (e.g. wheelchair access, other)
o how did you hear from us
• TESTIMONIALS/FEEDBACK
I can upload the logo design file upon your request (please specify the type of file required).
In addition to the web design, please indicate if you can undertake the coding for this webpage and if so, please provide a quote.
Updates
Hi there,
Thanks for your interest in this project.
I have uploaded the logo in .jpg, .ai and .eps files. Please feel free to let me know if further information is required.
Best regards,
Marisol

```html
<!DOCTYPE html>
<html lang="en">
<head>
<meta charset="utf-8">
<title>Orla Dental Clinic</title>
<link rel="stylesheet" href="https://fonts.googleapis.com/css2?family=Open+Sans:wght@400;600;700&family=Arimo:wght@400;700&display=swap">
<style>
:root{
  --blue:#0096d6;
  --green:#a6ce39;
  --text:#666666;
  --dark:#333333;
  --line:#c8c8c8;
  --btn:#4a4a4a;
  --white:#ffffff;
}
*{margin:0;padding:0;box-sizing:border-box}
html,body{width:1200px;height:1075px;overflow:hidden;background:var(--white)}
body{position:relative;font-family:"Arimo",Arial,sans-serif;color:var(--text)}
.abs{position:absolute}

/* header */
.brand{left:120px;top:52px;display:flex;align-items:center;gap:10px;font-family:"Open Sans",sans-serif;font-weight:600;font-size:26px;color:var(--blue)}
.brand-dot{width:22px;height:22px;border-radius:50%;background:var(--green)}
.contact-title{right:120px;top:16px;font-family:"Open Sans",sans-serif;font-size:20px;color:var(--blue);width:175px;text-align:right;border-bottom:1px solid var(--green);padding-bottom:2px}
.address{right:119px;top:51px;font-size:13px;line-height:17px;text-align:right;width:180px}
.appointment{left:688px;top:96px;width:198px;height:32px;border-radius:3px;background:linear-gradient(#fafafa,#e4e4e4);box-shadow:0 2px 3px rgba(0,0,0,.25);font-family:"Open Sans",sans-serif;font-size:19px;text-align:center;line-height:30px;color:var(--green)}
.appointment span{color:var(--blue)}
.phone{right:119px;top:109px;display:flex;align-items:center;gap:2px;font-family:"Open Sans",sans-serif;font-size:18px;color:var(--green)}

/* nav */
.nav{left:120px;top:147px;width:960px;height:41px;border-top:1px solid var(--line);border-bottom:3px solid var(--blue);display:flex;font-size:14px}
.nav a{display:block;text-decoration:none;color:var(--text);text-align:center;line-height:38px;border-right:1px solid var(--line)}
.nav a:last-child{border-right:none}
.nav a.active{color:var(--blue)}
.dropdown{left:292px;top:191px;width:152px}
.dropdown div{height:26px;background:var(--green);color:var(--white);font-size:14px;line-height:24px;padding-left:10px;border-bottom:2px solid rgba(255,255,255,.6)}

/* hero */
.hero{left:120px;top:190px;width:960px;height:423px;background:linear-gradient(120deg,#d9d3cf 0%,#7a90b8 35%,#3f6fb8 60%,#6b89c0 80%,#d7b79a 100%);clip-path:polygon(0 0,100% 0,100% 394px,930px 100%,0 100%)}
.hero-panel{left:120px;top:433px;width:440px;height:180px;background:linear-gradient(90deg,rgba(60,60,60,.85),rgba(90,90,90,.55))}
.hero-title{left:140px;top:440px;font-family:"Open Sans",sans-serif;font-size:60px;color:var(--white);text-shadow:2px 2px 4px rgba(0,0,0,.5);letter-spacing:-1px}
.hero-title .g{color:var(--green)}.hero-title .b{color:var(--blue)}
.hero-sub{left:267px;top:506px;font-family:"Open Sans",sans-serif;font-size:36px;letter-spacing:2px;color:#111}
.hero-text{left:140px;top:559px;width:430px;font-weight:700;font-size:15px;line-height:18px;color:var(--white)}

/* columns */
.col{top:654px;width:293px}
.col-head{height:38px;color:var(--white);font-family:"Open Sans",sans-serif;font-weight:700;font-size:22px;line-height:38px;padding-left:13px;text-shadow:1px 1px 2px rgba(0,0,0,.4);clip-path:polygon(0 0,94.5% 0,100% 12px,100% 100%,0 100%)}
.blue{background:var(--blue)}.greenbg{background:var(--green)}
.col-shadow{height:12px;margin:1px 10px 0;background:radial-gradient(ellipse at top,rgba(0,0,0,.25),rgba(0,0,0,0) 70%)}
.col-text{font-size:13px;line-height:17px;margin-top:13px}
.col-text+.col-text{margin-top:11px}
.more{display:inline-block;width:66px;height:24px;border-radius:3px;background:var(--btn);color:var(--white);font-size:14px;line-height:24px;text-align:center}
.testi{display:flex;gap:18px;margin-top:16px}
.testi+.testi{margin-top:13px}
.testi-photo{flex:0 0 106px;width:106px;height:74px;border:1px solid #ddd;background:linear-gradient(#f3efe6,#d9b99a)}
.testi-body{width:169px}
.testi-quote,.testi-name,.testi-role{font-size:13px;line-height:17px}
.testi-name{color:var(--blue);margin-top:6px;padding-left:2px}
.testi-role{color:var(--dark);padding-left:2px}

/* footer */
.footer-line{left:120px;top:971px;width:960px;border-top:1px dotted #bbb}
.footer-nav{left:120px;top:998px;font-size:12px;color:var(--text);display:flex;gap:17px}
.footer-nav .active{color:var(--green)}
.copyright{left:120px;top:1025px;font-size:12px}
.social{right:120px;top:994px;display:flex;flex-direction:column;align-items:flex-end;gap:2px;font-size:11px;line-height:14px;color:var(--blue)}
.social span{display:flex;align-items:center;gap:4px}
.social i{width:8px;height:8px;background:var(--blue)}
</style>
</head>
<body>

<header>
  <div class="abs brand"><span class="brand-dot"></span>Orla Dental Clinic</div>
  <div class="abs contact-title">Contact Us</div>
  <div class="abs address">Arcu erat molestie elit, in bibe ndum purus nibh ut metu usque lobortis, nisl id lac</div>
  <div class="abs appointment">Online <span>Appointment</span></div>
  <div class="abs phone">
    <svg width="20" height="24" viewBox="0 0 20 24"><path d="M5 1 L9 6 L6.5 9 C8 13 10 16 13 18 L16 15.5 L20 20 L16.5 23.5 C9 22 2 13 1 5 Z" fill="#333"/></svg>
    55-0142-7730
  </div>
</header>

<nav class="abs nav">
  <a style="width:76px">Home</a>
  <a style="width:97px">About Us</a>
  <a class="active" style="width:120px">Our Services</a>
  <a style="width:100px">Our Team</a>
  <a style="width:134px">Our Technology</a>
  <a style="width:84px">Gallery</a>
  <a style="width:126px">Special Offers</a>
  <a style="width:117px">Latest News</a>
  <a style="width:106px">Contact Us</a>
</nav>

<section>
  <div class="abs hero" role="img" aria-label="Photo of a group of smiling friends looking down into the camera against a blue sky"></div>
  <div class="abs hero-panel"></div>
  <div class="abs hero-title"><span class="g">A</span>liquam <span class="b">F</span>aucibus</div>
  <div class="abs hero-sub">MAURIS EUISMOD</div>
  <div class="abs hero-text">Phasellus lacinia, nunc sit amet tincidunt eleifend, arcu erat molestie elit, in bibendum purus nibh ut metus.</div>
  <div class="abs dropdown">
    <div>› Menu 1</div><div>› Menu 2</div><div>› Menu 3</div><div>› Menu 4</div>
  </div>
</section>

<main>
  <div class="abs col" style="left:120px">
    <div class="col-head blue">Welcome</div>
    <div class="col-shadow"></div>
    <p class="col-text">Ullam pharetra neque nec leo scelerisque lobortis. Morbi iaculis urna ut velit varius gravida. Quisque molestie massa non nisl porttitor vel sagittis nibh molestie.</p>
    <p class="col-text">Vivamus consectetur, sapien sed fringilla dapibus, tortor nisi ultrices nunc, ac eleifend sem risus at odio. Nunc eleifend mi in erat dignissim ullamco per. Sed scelerisque aliquam elit eget iaculis. Suspendisse vel mauris</p>
    <div class="more" style="margin-top:17px">More</div>
  </div>

  <div class="abs col" style="left:453px">
    <div class="col-head greenbg">Visit our Dental Clinic</div>
    <div class="col-shadow"></div>
    <p class="col-text">Pharetra neque nec leo scelerisque lobortis. Morbi iaculis urna ut velit varius gravida. Quisque mole stie massa non nisl porttitor vel sagittis nibh molestie.</p>
    <p class="col-text">Consectetur, sapien sed fringilla dapibus, tortor nisi ultrices nunc, ac eleifend sem risus at odio. Nunc eleifend mi in erat dignissim ullamco per. Sed scelerisque aliquam elit eget iaculis. Suspendisse vel mauris</p>
    <div class="more" style="margin-top:17px">More</div>
  </div>

  <div class="abs col" style="left:787px">
    <div class="col-head blue">Testimonials</div>
    <div class="col-shadow"></div>
    <div class="testi">
      <div class="testi-photo" role="img" aria-label="Portrait photo of a smiling patient"></div>
      <div class="testi-body"><p class="testi-quote">Donec et dui id mauris ege stas placerat.</p><p class="testi-name">Dorian P.</p><p class="testi-role">Nunc sit amet tincidunt</p></div>
    </div>
    <div class="testi">
      <div class="testi-photo" role="img" aria-label="Portrait photo of a smiling patient"></div>
      <div class="testi-body"><p class="testi-quote">Donec et dui id mauris ege stas placerat.</p><p class="testi-name">Greta L.</p><p class="testi-role">Nunc sit amet tincidunt</p></div>
    </div>
    <div class="more" style="margin-top:13px">More</div>
  </div>
</main>

<footer>
  <div class="abs footer-line"></div>
  <div class="abs footer-nav">
    <span class="active">Home</span><span>-</span><span>About Us</span><span>-</span><span>Our Services</span><span>-</span><span>Our Team</span><span>-</span><span>Our Technology</span><span>-</span><span>Gallery</span><span>-</span><span>Special Offers</span><span>-</span><span>Latest News</span><span>-</span><span>Contact Us</span>
  </div>
  <div class="abs social"><span><i></i>chatterbox</span><span><i></i>quillpost</span></div>
  <div class="abs copyright">Copyright © 2012 Orla Dental Clinic</div>
</footer>

</body>
</html>
```